Business Card Design Project

Hi!
Looking for a business card design for my acupuncture/remedial massage business using a logo I've just had designed through this site!
I'd like the following details included:
Logo (obviously)
My name - Marnie Trevaskis
Clinic details -Integrative Wellbeing and Natural Therapies Centre
42 Wendover Street
Kelburn Heights 3152
03 9471 2856
Website - www.trevaskisflow.com.au
I have the logo design in two different colour combinations, one predominantly green, and the other in reverse colours. I was thinking that the green logo would take up one whole side of the business card, then we could include the reverse logo on the more detailed side. I'd like to see how that looks.
I also had the idea that the heart in the logo could be printed in metallic red (depending on cost). Not sure if that comes into play now or at the printers.
Thanks!

```html
<!DOCTYPE html>
<html lang="en">
<head>
<meta charset="utf-8">
<title>Trevaskis Flow – Business Card</title>
<link rel="stylesheet" href="https://fonts.googleapis.com/css2?family=Roboto:wght@400;500;700&family=Roboto+Condensed:wght@400&display=swap">
<style>
  :root {
    --green: #1fc592;
    --green-deep: #19b07f;
    --green-text: #1eb88a;
    --white: #ffffff;
    --gap: #ffffff;
    --card-edge: #ececec;
  }
  * { margin: 0; padding: 0; box-sizing: border-box; }
  html, body {
    width: 1200px; height: 331px; overflow: hidden;
    background: var(--gap);
    font-family: "Roboto", Arial, sans-serif;
  }
  .sheet { position: relative; width: 1200px; height: 331px; }

  .card { position: absolute; top: 0; height: 331px; overflow: hidden; }

  /* Front */
  .card-front {
    left: 0; width: 588px;
    background: radial-gradient(ellipse at 50% 40%, var(--green) 0%, var(--green) 55%, var(--green-deep) 100%);
  }
  .front-mark {
    position: absolute; inset: 0;
    display: flex; align-items: center; justify-content: center; gap: 16px;
  }
  .front-mark .dot {
    width: 26px; height: 26px; border-radius: 50%; background: var(--white);
  }
  .front-mark .brand {
    color: var(--white); font-weight: 700; font-size: 52px; line-height: 1;
    letter-spacing: 0.5px;
  }

  /* Back */
  .card-back {
    left: 612px; width: 588px;
    background: var(--white);
    border: 1px solid var(--card-edge);
  }
  .clinic-title {
    position: absolute; left: 0; right: 0; top: 36px;
    text-align: center; color: var(--green-text);
    font-weight: 700; font-size: 21px; line-height: 32px;
  }
  .holder-name {
    position: absolute; left: 40px; top: 164px;
    color: var(--green-text); font-weight: 700; font-size: 19px;
  }
  .contact-list {
    position: absolute; left: 40px; top: 212px; list-style: none;
    font-family: "Roboto Condensed", Arial, sans-serif;
    font-size: 15px; color: var(--green-text);
  }
  .contact-list li { display: flex; align-items: flex-start; line-height: 22px; height: 22.5px; }
  .contact-list .icon { width: 14px; height: 14px; margin: 4px 17px 0 0; flex: none; fill: var(--green-text); }
  .contact-list .no-icon { width: 31px; flex: none; }

  .back-mark {
    position: absolute; left: 390px; top: 180px;
    display: flex; align-items: center; gap: 10px;
  }
  .back-mark .dot { width: 16px; height: 16px; border-radius: 50%; background: var(--green-text); flex: none; }
  .back-mark .brand {
    color: var(--green-text); font-weight: 700; font-size: 34px; line-height: 38px;
  }
  .base-band {
    position: absolute; left: 0; right: 0; bottom: 0; height: 12px;
    background: var(--green);
  }
</style>
</head>
<body>
<main class="sheet">
  <section class="card card-front" aria-label="Card front">
    <div class="front-mark">
      <span class="dot"></span>
      <span class="brand">Trevaskis Flow</span>
    </div>
  </section>

  <section class="card card-back" aria-label="Card back">
    <h1 class="clinic-title">Integrative Wellbeing &amp;<br>Natural Therapies Centre</h1>
    <h2 class="holder-name">Marnie Trevaskis</h2>
    <ul class="contact-list">
      <li>
        <svg class="icon" viewBox="0 0 14 14" aria-hidden="true"><path d="M7 0a5 5 0 0 0-5 5c0 3.6 5 9 5 9s5-5.4 5-9a5 5 0 0 0-5-5zm0 7a2 2 0 1 1 0-4 2 2 0 0 1 0 4z"/></svg>
        <span>42 Wendover Street</span>
      </li>
      <li><span class="no-icon"></span><span>Kelburn Heights 3152</span></li>
      <li>
        <svg class="icon" viewBox="0 0 14 14" aria-hidden="true"><path d="M3 1l2.2 2.6-1.2 1.6c.8 1.8 2.2 3.2 4 4l1.6-1.2L12.2 10 11 12.6C6 12 2 8 1.4 3z"/></svg>
        <span>03 9471 2856</span>
      </li>
      <li>
        <svg class="icon" viewBox="0 0 14 14" aria-hidden="true"><path d="M7 1a6 6 0 1 0 0 12A6 6 0 0 0 7 1zm4.5 5.3H9.6a9 9 0 0 0-.8-3.5 4.7 4.7 0 0 1 2.7 3.5zM7 2.4c.6.8 1.2 2.2 1.3 3.9H5.7C5.8 4.6 6.4 3.2 7 2.4zM5.2 2.8a9 9 0 0 0-.8 3.5H2.5a4.7 4.7 0 0 1 2.7-3.5zM2.5 7.7h1.9a9 9 0 0 0 .8 3.5 4.7 4.7 0 0 1-2.7-3.5zM7 11.6c-.6-.8-1.2-2.2-1.3-3.9h2.6c-.1 1.7-.7 3.1-1.3 3.9zm1.8-.4a9 9 0 0 0 .8-3.5h1.9a4.7 4.7 0 0 1-2.7 3.5z"/></svg>
        <span>www.trevaskisflow.com.au</span>
      </li>
    </ul>
    <div class="back-mark">
      <span class="dot"></span>
      <span class="brand">Trevaskis<br>Flow</span>
    </div>
    <div class="base-band"></div>
  </section>
</main>
</body>
</html>
```